RT7 church inspiring foldout brochure/booklet

RT7, a non-denominational christian church needs a full color, creative foldout brochure that provides next steps for guests who come to know Jesus. We want to provide basic information in a creative way as the first step in the follow-up process. We are in the midst of re-branding and would like the brochure to reflect relationship and the power we have when in relationship to affect change, etc.; making a positive impact on each other, the community and the world. We want the design to be minimalist and friendly. We do Not want something that looks churchy or cliche Christian. The final design should communicate community. Our new church website is under construction, the old website may be helpful to express our vision and values but should not be looked to for design inspiration (www.rt7.example).
We're basing our outline and content off of Lanternway.com's "Steps to walk" manual (attached below). Our tagline is "The Power of a Connected Life."
Updates

Thank you all for your patience as I navigate this new process. I have updated the brief. Please let me know if there is anything further that would be helpful.

Project Deadline Extended
Reason: We would like to expand the pool of designers.

Project Deadline Extended
Reason: We have a couple of designs that we are looking at more closely and sending out for feedback.

Target Market(s)

Adults in the North Eastern United States aged 18-50. Persons with limited church or faith background. We're located in the historic business district of Bethlehem, PA, USA- between Philadelphia and New York City. We have an average age of 33 with the majority of our demographic base under the age of 30 (families and children). However, we frequently have guests come in from the surrounding neighborhood and shopping district.

Industry/Entity Type

Church

Colors
85abd2
0355a3
3176b5
faf289
fece3e
00a88f
33b7a4
a64599
9bcb3c

Requirements
Must have
• Our tagline should be featured somewhere in the brochure: "The power of a connected life." The emphasis is the on the power inherent in connecting/relationships/community.

We use Mac and Windows platforms running Microsoft Office Suite of Programs, as well as Pages et al. At this point in our design journey we need the ability to edit content. Content should be treated like place holders.
Nice to have
• Brochure could be square or a shape other than rectangular. Would appreciate the layout being other than tri-fold rectangular.

Colors below are merely suggestions based on some current building design schemes.
Should not have
• Should not use old-style, serif fonts like Times New Roman. Should not include cliche "Christian" iconography or imagery. We're not a typically "churchy" church.

```html
<!DOCTYPE html>
<html lang="en">
<head>
<meta charset="utf-8">
<title>RT7 – The Power of a Connected Life</title>
<link rel="stylesheet" href="https://fonts.googleapis.com/css2?family=Arimo:wght@400;700&display=swap">
<style>
  :root {
    --sky-deep: #2b7fcc;
    --sky-mid: #5fa5dc;
    --sky-light: #9fcbed;
    --band-blue: #36a5e0;
    --crowd-light: #e4d6c6;
    --crowd-mid: #b99c80;
    --ink: #1a1a1a;
    --white: #ffffff;
  }
  * { margin: 0; padding: 0; box-sizing: border-box; }
  html, body { width: 1200px; height: 933px; overflow: hidden; background: var(--white); }
  body { font-family: "Arimo", Arial, sans-serif; }
  .brochure { position: relative; width: 1200px; height: 933px; overflow: hidden; }

  .sky-photo {
    position: absolute; left: 0; top: 0; width: 791px; height: 933px;
    background: linear-gradient(200deg, var(--sky-light) 0%, var(--sky-mid) 40%, var(--sky-deep) 100%);
  }
  .panel-veil {
    position: absolute; left: 394px; top: 0; width: 397px; height: 933px;
    background: rgba(255,255,255,.14);
  }

  .tagline {
    position: absolute; left: 15px; top: 300px;
    color: var(--white); font-weight: 700; font-size: 69px; line-height: 82px;
  }

  .contact {
    position: absolute; left: 452px; top: 580px;
    font-style: normal; font-size: 17.5px; line-height: 21px; color: var(--ink);
  }
  .contact-row { position: relative; padding-left: 31px; margin-bottom: 20px; }
  .contact-row svg { position: absolute; left: 0; top: 3px; width: 20px; height: 16px; }
  .contact-row.tight { margin-bottom: 4px; }

  .church-mark {
    position: absolute; left: 563px; top: 846px;
    display: flex; align-items: center; gap: 7px;
    font-size: 17px; font-weight: 700; color: var(--ink);
  }
  .church-mark .dot { width: 20px; height: 20px; border-radius: 50%; background: var(--ink); }

  .people-photo { position: absolute; left: 791px; top: 0; width: 409px; height: 933px; }

  .cover-title {
    position: absolute; left: 819px; top: 789px;
    color: var(--white); font-weight: 700; font-size: 35px; line-height: 40px;
  }
  .cover-subtitle {
    position: absolute; left: 819px; top: 833px;
    color: var(--white); font-weight: 700; font-size: 20.5px; line-height: 24px;
  }
</style>
</head>
<body>
<main class="brochure">
  <div class="sky-photo" role="img" aria-label="Bright blue sky with soft white clouds"></div>
  <div class="panel-veil"></div>

  <h1 class="tagline">The<br>Power of a<br>Connected<br>Life</h1>

  <address class="contact">
    <div class="contact-row">
      <svg viewBox="0 0 20 16"><path d="M10 1 L19 9 H16 V15 H12 V10 H8 V15 H4 V9 H1 Z" fill="#1a1a1a"/></svg>
      Ridgeline Together<br>Community Church<br>48 W. Linden Street<br>Lakeview, PA 18000 U.S.A.
    </div>
    <div class="contact-row">
      <svg viewBox="0 0 20 16"><path d="M2 6 C2 2 18 2 18 6 L15 7 L14 5 H6 L5 7 Z M6 7 H14 L17 13 H3 Z" fill="#1a1a1a"/></svg>
      555-014-2280 (p)<br>555.014.2291 (f)
    </div>
    <div class="contact-row tight">
      <svg viewBox="0 0 20 16"><rect x="2" y="3" width="16" height="11" fill="none" stroke="#1a1a1a" stroke-width="1.6"/><path d="M2 3 L10 10 L18 3" fill="none" stroke="#1a1a1a" stroke-width="1.6"/></svg>
      info@rt7.example
    </div>
    <div class="contact-row tight">
      <svg viewBox="0 0 20 16"><rect x="4" y="2" width="13" height="13" fill="#1a1a1a"/></svg>
      www.social.example/RT7church
    </div>
  </address>

  <div class="church-mark"><span class="dot"></span>RT7</div>

  <svg class="people-photo" viewBox="0 0 409 933">
    <defs>
      <linearGradient id="crowdTone" x1="0" y1="0" x2="0" y2="1">
        <stop offset="0" stop-color="#ffffff"/>
        <stop offset="0.3" stop-color="#e4d6c6"/>
        <stop offset="0.75" stop-color="#b99c80"/>
        <stop offset="1" stop-color="#e9e4df"/>
      </linearGradient>
    </defs>
    <rect width="409" height="933" fill="#ffffff"/>
    <rect x="0" y="150" width="409" height="640" fill="url(#crowdTone)" role="img" aria-label="Group of smiling friends cheering together"/>
    <path d="M0 765 Q200 745 409 748 V933 H0 Z" fill="#36a5e0"/>
  </svg>

  <h2 class="cover-title">Saved! Now What?</h2>
  <p class="cover-subtitle">Foundations for Living</p>
</main>
</body>
</html>
```